New business card design needed for Trucking/Staffing company!

I am looking for a business card design. The business name is Harbor Lane Freightworks, LLC. This company is a staffing company for commercial drivers/truck drivers. Most of our customers are trucking/supply companies. Our colors are blue/black/white/grey. The info I have on my current business cards is
-Spot for a name
-2 lines for an address
-3 lines for Office, cell, and fax
-email
-website(currently on backside of card with logo but can go anywhere)
Updates

Project Deadline Extended
Reason: Open to more designs

Target Market(s)

Trucking companies, building supply companies

Industry/Entity Type

Business

Contact Information for Business Card

Edgy but professional

Font styles to use
Other font styles liked:
• Open to suggestions

Colors
0555a3
000000
ffffff
9d9d9d

Requirements
Must have
• Must have the logo incorporated

```html
<!DOCTYPE html>
<html lang="en">
<head>
<meta charset="utf-8">
<title>Harbor Lane Freightworks, LLC — Business Card</title>
<link href="https://fonts.googleapis.com/css2?family=Open+Sans:wght@400;600;800&display=swap" rel="stylesheet">
<style>
  :root {
    --brand-blue: #3448b8;
    --brand-blue-deep: #2a3aa6;
    --ink: #000000;
    --paper: #f4f4f4;
    --grey: #9d9d9d;
    --text-dark: #1c1c1c;
    --backdrop: #d9d6d0;
  }
  html, body {
    margin: 0;
    padding: 0;
    width: 1200px;
    height: 780px;
    overflow: hidden;
    background: var(--backdrop);
    font-family: "Open Sans", Arial, sans-serif;
  }
  .sheet {
    position: relative;
    width: 1200px;
    height: 780px;
    display: flex;
    align-items: center;
    justify-content: center;
    gap: 60px;
  }
  .card {
    position: relative;
    width: 520px;
    height: 297px;
    box-shadow: 0 6px 18px rgba(0,0,0,0.25);
    overflow: hidden;
  }

  /* Front */
  .card-front { display: flex; flex-direction: column; }
  .front-brand-band {
    background: var(--ink);
    height: 104px;
    display: flex;
    align-items: center;
    padding-left: 34px;
    gap: 12px;
  }
  .brand-mark {
    width: 14px;
    height: 14px;
    background: var(--brand-blue);
  }
  .brand-name {
    font-weight: 800;
    font-size: 24px;
    letter-spacing: 0.5px;
    color: var(--brand-blue);
    text-transform: uppercase;
  }
  .front-contact-band {
    background: var(--paper);
    flex: 1;
    padding: 16px 34px 0 34px;
    font-size: 13px;
    line-height: 17px;
    color: var(--text-dark);
  }
  .address { margin: 0 0 4px 0; }
  .contact-list {
    display: grid;
    grid-template-columns: 56px auto;
    margin: 0;
  }
  .contact-list dt { color: var(--brand-blue); }
  .contact-list dd { margin: 0; }
  .front-name-band {
    background: linear-gradient(180deg, var(--brand-blue), var(--brand-blue-deep));
    height: 58px;
    display: flex;
    flex-direction: column;
    align-items: flex-end;
    justify-content: center;
    padding-right: 30px;
    color: #ffffff;
  }
  .employee-name {
    font-size: 17px;
    font-weight: 600;
    letter-spacing: 0.5px;
    line-height: 20px;
  }
  .employee-title { font-size: 12px; line-height: 14px; }

  /* Back */
  .card-back { display: flex; flex-direction: column; }
  .back-brand-field {
    flex: 1;
    background: radial-gradient(circle at 50% 40%, #3d52c6, var(--brand-blue-deep));
    display: flex;
    align-items: center;
    justify-content: center;
    gap: 12px;
  }
  .back-brand-field .brand-mark { background: #ffffff; }
  .back-brand-field .brand-name { color: #ffffff; font-size: 25px; }
  .back-web-strip {
    height: 40px;
    background: var(--paper);
    display: flex;
    align-items: center;
    padding-left: 34px;
    font-size: 14px;
    color: var(--brand-blue-deep);
  }
</style>
</head>
<body>
<main class="sheet">
  <section class="card card-front" aria-label="Business card front">
    <div class="front-brand-band">
      <span class="brand-mark"></span>
      <span class="brand-name">Harbor Lane Freightworks, LLC</span>
    </div>
    <div class="front-contact-band">
      <p class="address">PO BOX your address<br>harborview ny 10000</p>
      <dl class="contact-list">
        <dt>office</dt><dd>: 000 .1234 .5678</dd>
        <dt>mobile</dt><dd>: 000 .9876 .5432</dd>
        <dt>fax</dt><dd>: 000 .1234 .5679</dd>
        <dt>email</dt><dd>: hello@harborlanefreight.com</dd>
      </dl>
    </div>
    <div class="front-name-band">
      <span class="employee-name">EMPLOYEE NAME</span>
      <span class="employee-title">Owner</span>
    </div>
  </section>

  <section class="card card-back" aria-label="Business card back">
    <div class="back-brand-field">
      <span class="brand-mark"></span>
      <span class="brand-name">Harbor Lane Freightworks, LLC</span>
    </div>
    <div class="back-web-strip">www.harborlanefreight.com</div>
  </section>
</main>
</body>
</html>
```